Bright Harbor Construction

We are a commercial construction company specializing in steel stud framing, drywall, taping and acoustical ceilings. We would like a company logo (Something that looks great and isnt boring) as we have not been able to come up with one. A modern looking card would definitely suit our personalities best

We would like to try and avoid using dark colors. I have learned from experience that dark colors are the last to looked at. Thank you

```html
<!DOCTYPE html>
<html lang="en">
<head>
<meta charset="utf-8">
<title>Bright Harbor Construction – Business Card</title>
<link rel="stylesheet" href="https://fonts.googleapis.com/css2?family=Montserrat:wght@600;700&family=Questrial&display=swap">
<style>
  :root {
    --page: #e9e6e1;
    --card-light: #f3f3f4;
    --orange: #f9af3f;
    --orange-soft: #fbc26c;
    --gray: #6d6e71;
    --gray-faint: #e6e6e8;
    --text: #58595b;
    --white: #ffffff;
  }
  * { box-sizing: border-box; margin: 0; padding: 0; }
  html, body {
    width: 1131px; height: 1200px; overflow: hidden;
    background: var(--page);
    font-family: "Questrial", "Century Gothic", sans-serif;
  }
  .card {
    position: absolute;
    left: 178px;
    width: 776px;
    height: 443px;
    border-radius: 26px;
    overflow: hidden;
    box-shadow: 0 18px 26px rgba(0,0,0,0.22);
  }
  /* Front */
  .card-front { top: 100px; background: var(--card-light); }
  .front-band { position: absolute; left: 0; bottom: 0; height: 17px; width: 100%; display: flex; }
  .front-band .band-orange { flex: 0 0 387px; background: var(--orange); }
  .front-band .band-gray { flex: 1; background: var(--gray); margin-left: 3px; }
  .faint-name {
    position: absolute; left: 205px; top: 282px;
    font-family: "Montserrat", sans-serif; font-weight: 700;
    font-size: 74px; letter-spacing: 1px; color: var(--gray-faint);
    white-space: nowrap;
  }
  .brand-mark {
    position: absolute; display: flex; align-items: center; gap: 10px;
    font-family: "Montserrat", sans-serif; font-weight: 700; white-space: nowrap;
  }
  .card-front .brand-mark { left: 78px; top: 202px; font-size: 30px; color: var(--gray); }
  .brand-square { display: inline-block; background: var(--orange); }
  .card-front .brand-square { width: 22px; height: 22px; }
  .divider-line { position: absolute; left: 385px; top: 115px; width: 2px; height: 170px; background: var(--orange); opacity: 0.7; }
  .contact { position: absolute; left: 443px; top: 95px; color: var(--text); }
  .contact .person-name { font-size: 26px; letter-spacing: 0.5px; color: var(--gray); }
  .contact .person-name .first { color: var(--orange); }
  .contact .role { font-size: 18px; margin-top: 4px; }
  .contact .address { font-size: 20px; line-height: 25px; margin-top: 20px; }
  .contact .links { list-style: none; margin-top: 20px; font-size: 20px; line-height: 25px; }
  .contact .links li { display: flex; align-items: center; gap: 14px; }
  .contact .links svg { width: 12px; height: 12px; flex: none; }

  /* Back */
  .card-back { top: 620px; background: var(--orange); }
  .back-shapes { position: absolute; inset: 0; }
  .card-back .brand-mark { left: 50%; top: 118px; transform: translateX(-50%); font-size: 44px; color: var(--white); gap: 12px; }
  .card-back .brand-square { width: 28px; height: 28px; background: var(--white); }
  .company-name {
    position: absolute; left: 0; width: 100%; top: 234px; text-align: center;
    font-family: "Montserrat", sans-serif; font-weight: 600; font-size: 40px;
    color: var(--white); letter-spacing: 0.5px;
  }
  .company-sub {
    position: absolute; left: 50%; top: 290px; transform: translateX(-50%);
    display: flex; align-items: center; gap: 12px;
    font-size: 26px; color: var(--white); white-space: nowrap;
  }
  .company-sub .rule { width: 105px; height: 2px; background: var(--white); }
</style>
</head>
<body>

<section class="card card-front" aria-label="Business card front">
  <div class="faint-name" aria-hidden="true">Bright Harbor</div>
  <div class="brand-mark"><span class="brand-square"></span>Bright Harbor</div>
  <div class="divider-line"></div>
  <div class="contact">
    <p class="person-name"><span class="first">MARLO</span> DENSETT</p>
    <p class="role">owner</p>
    <p class="address">48 Cedar Row,<br>3rd FL Hartwell,<br>NY 10422</p>
    <ul class="links">
      <li><svg viewBox="0 0 12 12"><circle cx="6" cy="6" r="5" fill="var(--orange)"/></svg>brightharborbuild</li>
      <li><svg viewBox="0 0 12 12"><rect x="0.5" y="2" width="11" height="8" rx="1" fill="var(--orange)"/><path d="M1 2.5 6 6.5 11 2.5" stroke="var(--white)" stroke-width="1" fill="none"/></svg>hello@brightharborbuild.com</li>
      <li><svg viewBox="0 0 12 12"><rect x="1" y="1" width="10" height="10" fill="var(--orange)"/></svg>www.brightharborbuild.com</li>
    </ul>
  </div>
  <div class="front-band"><span class="band-orange"></span><span class="band-gray"></span></div>
</section>

<section class="card card-back" aria-label="Business card back">
  <svg class="back-shapes" viewBox="0 0 776 443" preserveAspectRatio="none" aria-hidden="true">
    <rect x="0" y="388" width="776" height="55" fill="var(--white)" opacity="0.12"/>
    <polygon points="615,275 776,275 776,443 453,443" fill="var(--white)" opacity="0.15"/>
  </svg>
  <div class="brand-mark"><span class="brand-square"></span>Bright Harbor</div>
  <h1 class="company-name">BRIGHT HARBOR</h1>
  <p class="company-sub"><span class="rule"></span>Construction<span class="rule"></span></p>
</section>

</body>
</html>
```